Kestrel electrical letter head

Require a letter head to go with our new logo for our start up company. Something fresh and professional looking, also perhaps a "ghost"image of the logo in the centre of the page. Address to go on it PO Box 58, Harwick 7386. Web address: www.kestrel-example.net.nz

```html
<!DOCTYPE html>
<html lang="en">
<head>
<meta charset="utf-8">
<title>Kestrel Electrical – Letterhead</title>
<link href="https://fonts.googleapis.com/css2?family=Open+Sans:wght@600;700&display=swap" rel="stylesheet">
<style>
  :root {
    --brand-blue: #3d78c0;
    --brand-green: #a8cf3c;
    --ghost-blue: #b9cde6;
    --paper: #ffffff;
  }
  html, body {
    margin: 0;
    padding: 0;
    width: 911px;
    height: 1200px;
    overflow: hidden;
    background: var(--paper);
  }
  .letterhead {
    position: relative;
    width: 911px;
    height: 1200px;
    background: var(--paper);
    font-family: "Open Sans", Arial, sans-serif;
    overflow: hidden;
  }
  .brand {
    position: absolute;
    left: 40px;
    top: 62px;
    display: flex;
    align-items: center;
    gap: 14px;
  }
  .brand-dot {
    width: 46px;
    height: 46px;
    border-radius: 50%;
    background: var(--brand-blue);
  }
  .brand-name {
    margin: 0;
    font-size: 44px;
    font-weight: 700;
    color: var(--brand-blue);
    letter-spacing: 0.5px;
    line-height: 1;
  }
  .contact {
    position: absolute;
    left: 580px;
    top: 44px;
    margin: 0;
    padding: 0;
    list-style: none;
  }
  .contact-item {
    display: flex;
    align-items: center;
    height: 32px;
    color: var(--brand-blue);
    font-size: 19px;
    font-weight: 600;
    white-space: nowrap;
  }
  .contact-item svg {
    width: 30px;
    height: 26px;
    margin-right: 14px;
    flex: none;
  }
  .contact-phone { letter-spacing: 2px; }
  .ghost-mark {
    position: absolute;
    left: 640px;
    top: 790px;
    width: 320px;
    height: 320px;
    border-radius: 50%;
    background: var(--ghost-blue);
    opacity: 0.55;
  }
  .footer-bands {
    position: absolute;
    left: 0;
    top: 1128px;
    width: 911px;
    height: 30px;
  }
</style>
</head>
<body>
<div class="letterhead">
  <header class="brand">
    <div class="brand-dot"></div>
    <h1 class="brand-name">Kestrel Electrical</h1>
  </header>

  <ul class="contact">
    <li class="contact-item contact-phone">
      <svg viewBox="0 0 30 26" aria-hidden="true">
        <path d="M2 8 Q15 0 28 8 L26 12 L21 10 L20 7 Q15 5 10 7 L9 10 L4 12 Z" fill="var(--brand-blue)"/>
        <path d="M7 12 L23 12 L27 24 L3 24 Z" fill="var(--brand-blue)"/>
        <circle cx="15" cy="18" r="3.5" fill="var(--paper)"/>
      </svg>
      0800 555 214
    </li>
    <li class="contact-item">
      <svg viewBox="0 0 30 26" aria-hidden="true">
        <rect x="1" y="8" width="16" height="10" fill="none" stroke="var(--brand-blue)" stroke-width="2"/>
        <path d="M1 8 L9 14 L17 8" fill="none" stroke="var(--brand-blue)" stroke-width="2"/>
        <rect x="16" y="6" width="12" height="14" rx="2" fill="var(--brand-blue)"/>
        <rect x="20" y="18" width="4" height="8" fill="var(--brand-blue)"/>
        <rect x="22" y="0" width="2" height="7" fill="var(--brand-blue)"/>
      </svg>
      PO Box 58, Harwick 7386
    </li>
    <li class="contact-item">
      <svg viewBox="0 0 30 26" aria-hidden="true">
        <g fill="none" stroke="var(--brand-blue)" stroke-width="2">
          <circle cx="15" cy="13" r="11"/>
          <ellipse cx="15" cy="13" rx="5" ry="11"/>
          <line x1="4" y1="13" x2="26" y2="13"/>
          <line x1="6" y1="7" x2="24" y2="7"/>
          <line x1="6" y1="19" x2="24" y2="19"/>
        </g>
      </svg>
      www.kestrel-example.net.nz
    </li>
  </ul>

  <div class="ghost-mark" aria-hidden="true"></div>

  <svg class="footer-bands" viewBox="0 0 911 30" aria-hidden="true">
    <polygon points="0,4 768,4 773,9 0,9" fill="var(--brand-green)"/>
    <polygon points="0,18 786,18 798,27 0,27" fill="var(--brand-blue)"/>
  </svg>
</div>
</body>
</html>
```